Business Card & Logo Design - Hedge Fund

We need a business card and logo design for a hedge fund. The hedge fund is named Morvane Equity LLC. Morvane Equity was created by finance professors and the strategy is based academic research that looks for patterns in stock prices. The design should look conservative, solid, strong. We favor a classic style - nothing flashy. The logo can relate to the name Morvane Equity, or it could involve a symbol design that connotes "science" . We are open to ideas. We do not want alot of colors - but if any, color - blue is preferred. The font that seems to look best for the name (Morvane Equity) is arial black. We are open to ideas. Most important - we want to see a mock up of an actual business card with the logo concept embedded. The business card should include space for : company name, individual name, position title, cell phone, address. We hope to have this work done by Sept. 8.

Target Market(s)

We will be meeting with and giving the business card to institutions and high net worth individuals.

Industry/Entity Type

Investment Advisory

Contact Information for Business Card

Company name - Morvane Equity LLC
Individual name - Peter Dalby
Title - Portfolio Manager
Cell - (412) 555-0187
Address - 2650 Birchmont Lane, Suite 300, Atlanta GA 30327

Font styles to use
Other font styles liked:
• Arial

Colors
3277b5
0255a3
85acd3
cedeed
fdf9cf
d9d9d9
e6e6e6
f04a50
6b449b

Requirements
Must have
• Must have card details that are sited above.
• We would like a logo related to the name (Morvane Equity) or concept of the fund.
Nice to have
• We want conservative / understated / clean crisp look.
• If any colors - we prefer conservative appearance - blue / gray.
• I have enclosed an example of a card style that looks attractive - please do not exactly copy this card. This is not our company or logo. I feel the layout is attractive - just as an example
Should not have
• Avoid too much color.
• I have selected some preferred colors. Please do not use all of the colors - I have selected a few that might work - but I am not sure. We are open to your ideas so please do not feel the need to use all or any of these.

```html
<!DOCTYPE html>
<html lang="en">
<head>
<meta charset="utf-8">
<title>Morvane Equity LLC – Business Card</title>
<link rel="stylesheet" href="https://fonts.googleapis.com/css2?family=Arimo:wght@400;700&display=swap">
<style>
  :root {
    --stage: #161616;
    --card: #232323;
    --card-edge: #2d2d2d;
    --silver: #c9c9c9;
    --grey-text: #a8a8a8;
    --rule: #5a5a5a;
    --blue: #2a2aa0;
  }
  * { margin: 0; padding: 0; box-sizing: border-box; }
  html, body { width: 1200px; height: 900px; overflow: hidden; background: var(--stage); }
  body { position: relative; font-family: "Arimo", Arial, sans-serif; }

  .card {
    position: absolute;
    width: 560px;
    height: 320px;
    background: var(--card);
    border: 1px solid var(--card-edge);
    border-radius: 26px;
    box-shadow: 0 18px 40px rgba(0,0,0,.55);
  }
  .card--front { left: 250px; top: 90px; }
  .card--back  { left: 390px; top: 480px; }

  .wordmark {
    position: absolute;
    display: flex;
    align-items: center;
    gap: 12px;
    font-weight: 700;
    text-transform: uppercase;
    letter-spacing: .5px;
    color: var(--silver);
    white-space: nowrap;
  }
  .wordmark__square { width: 16px; height: 16px; background: var(--silver); }
  .card--front .wordmark { left: 0; right: 0; top: 142px; justify-content: center; font-size: 26px; }
  .card--back .wordmark { right: 40px; top: 52px; font-size: 20px; }

  .rule { position: absolute; height: 1px; background: var(--rule); }
  .rule--logo { left: 250px; right: 40px; top: 92px; }
  .rule--name { left: 210px; right: 40px; top: 206px; }

  .phone {
    position: absolute;
    right: 40px; top: 150px;
    display: flex; align-items: center; gap: 8px;
    font-size: 17px; color: var(--grey-text);
  }
  .phone svg { width: 14px; height: 16px; }

  .person { position: absolute; left: 40px; top: 194px; }
  .person__name { font-weight: 700; font-size: 19px; letter-spacing: .5px; color: var(--silver); }
  .person__first { color: var(--blue); }
  .person__title { font-size: 14px; color: var(--grey-text); margin-top: 3px; }
  .address { margin-top: 14px; font-size: 15px; line-height: 1.25; color: var(--grey-text); }
</style>
</head>
<body>
  <section class="card card--front" aria-label="Card front">
    <div class="wordmark"><span class="wordmark__square"></span>Morvane Equity LLC</div>
  </section>

  <section class="card card--back" aria-label="Card back">
    <div class="wordmark"><span class="wordmark__square"></span>Morvane Equity LLC</div>
    <div class="rule rule--logo"></div>

    <div class="phone">
      (412) 555-0187
      <svg viewBox="0 0 14 16" aria-hidden="true">
        <rect x="2" y="1" width="10" height="14" rx="2" fill="none" stroke="#2a2aa0" stroke-width="1.6"/>
        <rect x="5.5" y="12" width="3" height="1.4" fill="#2a2aa0"/>
      </svg>
    </div>

    <div class="rule rule--name"></div>
    <div class="person">
      <div class="person__name"><span class="person__first">PETER</span> DALBY</div>
      <div class="person__title">Portfolio Manager</div>
      <div class="address">
        MORVANE EQUITY LLC<br>
        2650 Birchmont Lane<br>
        Suite 300, Atlanta GA 30327
      </div>
    </div>
  </section>
</body>
</html>
```